International Legal Service Company needs Letterhead Design

Put my new Logo into Letterhead Design, using updated telephone number, e-mail address and website. Current letterhead and updated information which i want you to include my new letterhead attached herewith. Of course, my new Logo attached herein. Also, you can use slogan "Complete Legal Support Services For International Enterprises"

It Company

```html
<!DOCTYPE html>
<html lang="en">
<head>
<meta charset="utf-8">
<title>Meridian Counsel Partners Inc – Letterhead</title>
<link rel="stylesheet" href="https://fonts.googleapis.com/css2?family=Arimo:wght@400;700&display=swap">
<style>
  :root {
    --backdrop: #e6e6e6;
    --paper: #ffffff;
    --brand-blue: #1f3fb0;
    --label-blue: #1e3ca8;
    --ink: #111111;
    --rule: #555555;
  }
  * { margin: 0; padding: 0; box-sizing: border-box; }
  html, body {
    width: 1001px;
    height: 1200px;
    overflow: hidden;
    background: var(--backdrop);
    font-family: "Arimo", Arial, sans-serif;
    color: var(--ink);
  }
  .letterhead {
    position: absolute;
    left: 84px;
    top: 61px;
    width: 833px;
    height: 1078px;
    background: var(--paper);
  }
  .brand {
    position: absolute;
    left: 23px;
    top: 35px;
    display: flex;
    align-items: center;
  }
  .brand-mark {
    width: 88px;
    height: 88px;
    border-radius: 50%;
    background: var(--brand-blue);
    flex: none;
  }
  .brand-name {
    margin-left: 13px;
    padding-top: 8px;
    color: var(--brand-blue);
    font-weight: 400;
    line-height: 1.1;
  }
  .brand-name .line-main { display: block; font-size: 24px; }
  .brand-name .line-sub { display: block; font-size: 17px; letter-spacing: 1px; }
  .contact-block {
    position: absolute;
    left: 585px;
    top: 17px;
    height: 123px;
    border-left: 1px solid var(--rule);
    padding-left: 17px;
    font-size: 14.5px;
    line-height: 18.3px;
    font-style: normal;
  }
  .address { margin-bottom: 10px; padding-top: 1px; }
  .contact-list { list-style: none; }
  .contact-list .label {
    color: var(--label-blue);
    font-weight: 700;
    margin-right: 7px;
  }
  .slogan {
    position: absolute;
    left: 0;
    right: 0;
    top: 1041px;
    text-align: center;
    font-size: 13px;
    font-weight: 700;
  }
</style>
</head>
<body>
  <main class="letterhead">
    <header>
      <div class="brand">
        <div class="brand-mark" aria-hidden="true"></div>
        <div class="brand-name">
          <span class="line-main">Meridian Counsel</span>
          <span class="line-sub">Partners Inc</span>
        </div>
      </div>
      <address class="contact-block">
        <div class="address">
          1480 Lakeview Parkway<br>
          Suite 300, Fairbrook, MD 20911
        </div>
        <ul class="contact-list">
          <li><span class="label">T:</span>555-201-4830</li>
          <li><span class="label">F:</span>555-201-4831</li>
          <li><span class="label">E:</span>office@meridiancounsel.com</li>
          <li><span class="label">W:</span>www.meridiancounsel.com</li>
        </ul>
      </address>
    </header>
    <footer class="slogan">Complete Legal Support Services For International Enterprises</footer>
  </main>
</body>
</html>
```